Web Based Ordering. We have an existing input screen- Need to Clean it up

we have an existing ordering Modal on a trucking management system, but it looks and feels clunky. We would like to modernize the look and feel of it. We need to keep the same input fields, but we are open to any type of reconfiguration or layout changes you can think of to improve the flow and layout.

This design is for a web browser, not mobile app.

Target Market(s)

construction and trucking industry

Colors
85acd3
3176b5
33a6d7
85cae6
33b8a4
86cfc6

Requirements
Must have
• all the input fields displayed are required
Nice to have
• some of the fields can probably be combined to consolidate the number of tabs.

```html
<!DOCTYPE html>
<html lang="en">
<head>
<meta charset="utf-8">
<title>Haulway Freight – New Material Order</title>
<link href="https://fonts.googleapis.com/css2?family=Nunito:wght@400;600;700;800&display=swap" rel="stylesheet">
<style>
:root{
  --navy:#2a5fa6;
  --navy-dark:#1f4f8f;
  --teal:#2fae98;
  --teal-light:#86cfc6;
  --teal-faint:#9fded3;
  --sky:#dfe9f6;
  --stage:#5b5b5b;
  --stage-blue:#2a63a8;
  --ink:#2b2b2b;
  --muted:#5f6670;
  --line:#c9cfd7;
  --red:#e0242b;
  --white:#ffffff;
}
*{box-sizing:border-box;margin:0;padding:0}
html,body{width:1200px;height:883px;overflow:hidden;background:var(--stage)}
body{font-family:'Nunito',sans-serif;color:var(--ink)}
.stage{position:absolute;left:0;top:0;width:2245px;height:1652px;transform:scale(0.53452);transform-origin:0 0;background:var(--stage);overflow:hidden}
.stage-shapes{position:absolute;inset:0}
.screen{position:absolute;width:1043px;background:var(--sky);box-shadow:0 10px 30px rgba(0,0,0,.35);overflow:hidden}
.sidebar{position:absolute;left:0;top:0;bottom:0;width:70px;background:linear-gradient(180deg,var(--navy) 0%,#2a86a8 45%,var(--teal) 100%)}
.nav-item{position:absolute;left:0;width:70px;text-align:center;color:var(--white);font-size:10px}
.nav-item svg{display:block;margin:0 auto 4px}
.nav-item::after{content:"";position:absolute;left:4px;right:4px;bottom:-14px;height:1px;background:rgba(255,255,255,.15)}
.topbar{position:absolute;left:70px;right:0;top:0;height:70px;background:var(--white)}
.brand{position:absolute;left:35px;top:17px;font-size:29px;font-weight:800;color:var(--navy-dark);letter-spacing:.5px}
.search{position:absolute;left:562px;top:17px;width:308px;height:35px;border:1.5px solid #c9cdd3;border-radius:18px;font-size:10px;color:#555;padding:11px 0 0 22px}
.search-btn{position:absolute;right:3px;top:2px;width:28px;height:28px;border-radius:50%;background:var(--teal)}
.search-btn svg{position:absolute;left:7px;top:7px}
.icon-user{position:absolute;left:898px;top:24px}
.icon-bell{position:absolute;left:928px;top:23px}
.badge{position:absolute;left:942px;top:22px;width:12px;height:12px;border-radius:50%;background:var(--navy);color:#fff;font-size:8px;text-align:center;line-height:12px}
.page-title{position:absolute;left:98px;top:95px;font-size:33px;font-weight:600;color:#222}
.card{position:absolute;left:99px;width:912px;background:var(--white);box-shadow:0 1px 4px rgba(0,0,0,.08)}
.steps{position:absolute;left:118px;top:157px;width:874px;height:37px;background:var(--teal);display:flex;font-size:15px;font-weight:600;color:var(--white)}
.step{height:37px;display:flex;align-items:center;justify-content:center;gap:7px}
.step.todo{color:var(--teal-faint);font-weight:400}
.step.active{background:var(--navy)}
.step-edit{position:absolute;right:9px;top:5px}
.field-label{position:absolute;font-size:15px;font-weight:600;color:#333}
.field-label .req{color:var(--red)}
.field{position:absolute;height:41px;border:1.5px solid var(--line);border-radius:3px;font-size:10.5px;color:#333;padding:12px 0 0 16px;background:#fff}
.field .ctl{position:absolute;right:12px;top:13px;display:flex;gap:9px;align-items:center}
.btn{position:absolute;height:48px;border-radius:24px;font-size:16px;font-weight:600;color:#fff;display:flex;align-items:center;justify-content:center}
.btn.cancel{width:138px;background:var(--navy)}
.btn.continue{width:138px;background:var(--teal)}
.btn.outline{height:47px;border:2.5px solid var(--navy);background:#fff;color:var(--navy);font-size:13px;gap:9px}
.toggle{position:absolute;width:151px;height:41px;border:1.5px solid var(--line);display:flex;font-size:19px;font-weight:600}
.toggle span{display:flex;align-items:center;justify-content:center}
.toggle .off{width:73px;color:var(--navy);background:#fff}
.toggle .on{flex:1;color:#fff;background:var(--navy)}
.footer{position:absolute;left:70px;right:0;text-align:center;font-size:13px;color:#444}
</style>
</head>
<body>
<svg width="0" height="0" style="position:absolute">
  <symbol id="tick" viewBox="0 0 12 10"><path d="M1 5.2l3.2 3.2L11 1.5" fill="none" stroke="currentColor" stroke-width="2.4"/></symbol>
  <symbol id="clear" viewBox="0 0 8 8"><path d="M1 1l6 6M7 1L1 7" stroke="#777" stroke-width="1.8"/></symbol>
  <symbol id="caret" viewBox="0 0 8 5"><path d="M0 0h8L4 5z" fill="#777"/></symbol>
  <symbol id="spin" viewBox="0 0 6 10"><path d="M0 4h6L3 0zM0 6h6L3 10z" fill="#777"/></symbol>
  <symbol id="plus" viewBox="0 0 12 12"><circle cx="6" cy="6" r="6" fill="#2a5fa6"/><path d="M6 3v6M3 6h6" stroke="#fff" stroke-width="1.8"/></symbol>
  <symbol id="pencil" viewBox="0 0 28 28"><circle cx="14" cy="14" r="12.5" fill="none" stroke="#fff" stroke-width="1.8"/><path d="M9 19l1-3.5 6.5-6.5 2.5 2.5-6.5 6.5z" fill="#fff"/></symbol>
  <symbol id="gauge" viewBox="0 0 24 24"><path d="M12 3a10 10 0 0 0-9 14.5h18A10 10 0 0 0 12 3z" fill="#fff"/><circle cx="12" cy="15" r="2" fill="#2a5fa6"/><path d="M12 15l4-6" stroke="#2a5fa6" stroke-width="1.8"/><circle cx="6" cy="12" r="1.2" fill="#2a5fa6"/><circle cx="8" cy="8" r="1.2" fill="#2a5fa6"/><circle cx="12" cy="6.5" r="1.2" fill="#2a5fa6"/></symbol>
  <symbol id="info" viewBox="0 0 24 24"><circle cx="12" cy="12" r="11" fill="#fff"/><circle cx="12" cy="7" r="1.6" fill="#2a6fa8"/><path d="M10 10.5h3v7h1.5M9.5 17.5h5" stroke="#2a6fa8" stroke-width="2" fill="none"/></symbol>
  <symbol id="help" viewBox="0 0 24 24"><circle cx="12" cy="12" r="11" fill="#fff"/><path d="M9 9a3 3 0 1 1 4.5 2.6c-1 .6-1.5 1.2-1.5 2.4" stroke="#2a80a6" stroke-width="2.4" fill="none"/><circle cx="12" cy="17.5" r="1.5" fill="#2a80a6"/></symbol>
  <symbol id="gear" viewBox="0 0 24 24"><path d="M10 1h4l.6 3 2.4 1.2 2.6-1.7 2.8 2.8-1.7 2.6L22 11v4l-3 .6-1 2.4 1.7 2.6-2.8 2.8-2.6-1.7-2.4 1L11 23h-4"  fill="none"/><g fill="#fff"><circle cx="12" cy="12" r="7.5"/><rect x="10" y="1" width="4" height="5"/><rect x="10" y="18" width="4" height="5"/><rect x="1" y="10" width="5" height="4"/><rect x="18" y="10" width="5" height="4"/><rect x="10" y="1" width="4" height="5" transform="rotate(45 12 12)"/><rect x="10" y="18" width="4" height="5" transform="rotate(45 12 12)"/><rect x="1" y="10" width="5" height="4" transform="rotate(45 12 12)"/><rect x="18" y="10" width="5" height="4" transform="rotate(45 12 12)"/></g><circle cx="12" cy="12" r="3" fill="#2a96a4"/></symbol>
  <symbol id="lens" viewBox="0 0 14 14"><circle cx="6" cy="6" r="4.2" fill="none" stroke="#fff" stroke-width="2"/><path d="M9 9l3.5 3.5" stroke="#fff" stroke-width="2.2"/></symbol>
  <symbol id="user" viewBox="0 0 20 22"><circle cx="10" cy="7" r="5" fill="none" stroke="#222" stroke-width="1.8"/><path d="M1.5 21v-2a6 6 0 0 1 6-6h5a6 6 0 0 1 6 6v2z" fill="none" stroke="#222" stroke-width="1.8"/></symbol>
  <symbol id="bell" viewBox="0 0 22 22"><path d="M4 16c2-2 1.5-5 2.5-8a5 5 0 0 1 9.5 1c.5 3 0 5 2.5 7z" fill="none" stroke="#222" stroke-width="1.8" transform="rotate(-12 11 11)"/><path d="M8.5 19.5a2.5 2.5 0 0 0 4.5-.5" fill="none" stroke="#222" stroke-width="1.8"/></symbol>
</svg>

<div class="stage">
  <svg class="stage-shapes" width="2245" height="1652" viewBox="0 0 2245 1652">
    <polygon points="0,0 865,0 590,700 0,635" fill="var(--stage-blue)"/>
    <polygon points="1525,1080 2245,460 2245,1652 1620,1652" fill="var(--stage-blue)"/>
  </svg>

  <!-- Step 1: Date and Start -->
  <section class="screen" style="left:65px;top:75px;height:736px">
    <nav class="sidebar">
      <div class="nav-item" style="top:17px"><svg width="26" height="26"><use href="#gauge"/></svg>Dashboard</div>
      <div class="nav-item" style="top:97px"><svg width="25" height="25"><use href="#info"/></svg>Info</div>
      <div class="nav-item" style="top:180px"><svg width="25" height="25"><use href="#help"/></svg>Questions</div>
      <div class="nav-item" style="top:264px"><svg width="25" height="25"><use href="#gear"/></svg>Setings</div>
    </nav>
    <header class="topbar">
      <div class="brand">HAULWAY FREIGHT</div>
      <div class="search">Search<span class="search-btn"><svg width="14" height="14"><use href="#lens"/></svg></span></div>
      <svg class="icon-user" width="20" height="22"><use href="#user"/></svg>
      <svg class="icon-bell" width="22" height="22"><use href="#bell"/></svg>
      <span class="badge">3</span>
    </header>
    <h1 class="page-title">New Material Order</h1>
    <div class="card" style="top:157px;height:509px"></div>
    <div class="steps">
      <div class="step active" style="width:168px"><svg width="12" height="10"><use href="#tick"/></svg>Date and Start</div>
      <div class="step" style="width:169px"><svg width="12" height="10"><use href="#tick"/></svg>Destination</div>
      <div class="step todo" style="width:115px">Material</div>
      <div class="step" style="width:110px"><svg width="12" height="10"><use href="#tick"/></svg>Trucks</div>
      <div class="step" style="width:110px"><svg width="12" height="10"><use href="#tick"/></svg>Rates</div>
      <div class="step todo" style="width:135px">Summary</div>
      <svg class="step-edit" width="28" height="28"><use href="#pencil"/></svg>
    </div>
    <label class="field-label" style="left:139px;top:226px">Customer <span class="req">*</span></label>
    <div class="field" style="left:139px;top:258px;width:832px">R.T.Barlow Contracting Company,Inc.<span class="ctl"><svg width="8" height="8"><use href="#clear"/></svg><svg width="8" height="5"><use href="#caret"/></svg></span></div>
    <label class="field-label" style="left:139px;top:325px">Starting Location <span class="req">*</span></label>
    <div class="field" style="left:139px;top:357px;width:832px">2109-Ridgeway US 18/SR 5<span class="ctl"><svg width="8" height="8"><use href="#clear"/></svg><svg width="8" height="5"><use href="#caret"/></svg></span></div>
    <label class="field-label" style="left:139px;top:426px">Load Date <span class="req">*</span></label>
    <div class="field" style="left:139px;top:458px;width:402px">02/27/2021<span class="ctl" style="right:28px"><svg width="8" height="8"><use href="#clear"/></svg></span></div>
    <label class="field-label" style="left:582px;top:426px">Load Time <svg width="14" height="14" style="vertical-align:-2px;margin-left:3px"><circle cx="7" cy="7" r="5" fill="none" stroke="#e0242b" stroke-width="1.6" stroke-dasharray="2 1.4"/></svg></label>
    <div class="field" style="left:568px;top:458px;width:402px;padding-left:23px">6:00AM<span class="ctl" style="right:14px"><svg width="8" height="8"><use href="#clear"/></svg></span></div>
    <div class="btn cancel" style="left:139px;top:574px">CANCEL</div>
    <div class="btn continue" style="left:833px;top:574px">CONTINUE</div>
    <footer class="footer" style="top:698px">© 2021 Companyname.All Rights Reserved &nbsp;|&nbsp; Privacy Policy &nbsp;|&nbsp; Terms and Use</footer>
  </section>

  <!-- Step 3: Material -->
  <section class="screen" style="left:65px;top:841px;height:737px">
    <nav class="sidebar">
      <div class="nav-item" style="top:17px"><svg width="26" height="26"><use href="#gauge"/></svg>Dashboard</div>
      <div class="nav-item" style="top:97px"><svg width="25" height="25"><use href="#info"/></svg>Info</div>
      <div class="nav-item" style="top:180px"><svg width="25" height="25"><use href="#help"/></svg>Questions</div>
      <div class="nav-item" style="top:264px"><svg width="25" height="25"><use href="#gear"/></svg>Setings</div>
    </nav>
    <header class="topbar">
      <div class="brand">HAULWAY FREIGHT</div>
      <div class="search">Search<span class="search-btn"><svg width="14" height="14"><use href="#lens"/></svg></span></div>
      <svg class="icon-user" width="20" height="22"><use href="#user"/></svg>
      <svg class="icon-bell" width="22" height="22"><use href="#bell"/></svg>
      <span class="badge">3</span>
    </header>
    <h1 class="page-title">New Material Order</h1>
    <div class="card" style="top:157px;height:509px"></div>
    <div class="steps">
      <div class="step" style="width:168px"><svg width="12" height="10"><use href="#tick"/></svg>Date and Start</div>
      <div class="step" style="width:151px"><svg width="12" height="10"><use href="#tick"/></svg>Destination</div>
      <div class="step active" style="width:134px"><svg width="12" height="10"><use href="#tick"/></svg>Material</div>
      <div class="step" style="width:110px"><svg width="12" height="10"><use href="#tick"/></svg>Trucks</div>
      <div class="step" style="width:110px"><svg width="12" height="10"><use href="#tick"/></svg>Rates</div>
      <div class="step todo" style="width:135px">Summary</div>
      <svg class="step-edit" width="28" height="28"><use href="#pencil"/></svg>
    </div>
    <label class="field-label" style="left:139px;top:226px">Work type <span class="req">*</span></label>
    <div class="field" style="left:139px;top:258px;width:832px">Asphalt -Machine Paving<span class="ctl"><svg width="8" height="8"><use href="#clear"/></svg><svg width="8" height="5"><use href="#caret"/></svg></span></div>
    <label class="field-label" style="left:139px;top:328px">Material Type <span class="req">*</span></label>
    <div class="field" style="left:139px;top:360px;width:402px">02/27/2021<span class="ctl"><svg width="8" height="8"><use href="#clear"/></svg><svg width="8" height="5"><use href="#caret"/></svg></span></div>
    <label class="field-label" style="left:582px;top:328px">Tonnage <span class="req">*</span></label>
    <div class="field" style="left:568px;top:360px;width:402px;padding-left:23px">400<span class="ctl" style="right:13px;top:14px"><svg width="6" height="10"><use href="#spin"/></svg></span></div>
    <div class="btn outline" style="left:139px;top:432px;width:247px"><svg width="12" height="12"><use href="#plus"/></svg>ADDITIONAL MATERIAL</div>
    <div class="btn cancel" style="left:139px;top:574px">CANCEL</div>
    <div class="btn continue" style="left:833px;top:574px">CONTINUE</div>
    <footer class="footer" style="top:698px">© 2021 Companyname.All Rights Reserved &nbsp;|&nbsp; Privacy Policy &nbsp;|&nbsp; Terms and Use</footer>
  </section>

  <!-- Step 2: Destination -->
  <section class="screen" style="left:1137px;top:75px;height:1013px">
    <nav class="sidebar">
      <div class="nav-item" style="top:17px"><svg width="26" height="26"><use href="#gauge"/></svg>Dashboard</div>
      <div class="nav-item" style="top:97px"><svg width="25" height="25"><use href="#info"/></svg>Info</div>
      <div class="nav-item" style="top:180px"><svg width="25" height="25"><use href="#help"/></svg>Questions</div>
      <div class="nav-item" style="top:264px"><svg width="25" height="25"><use href="#gear"/></svg>Setings</div>
    </nav>
    <header class="topbar">
      <div class="brand">HAULWAY FREIGHT</div>
      <div class="search">Search<span class="search-btn"><svg width="14" height="14"><use href="#lens"/></svg></span></div>
      <svg class="icon-user" width="20" height="22"><use href="#user"/></svg>
      <svg class="icon-bell" width="22" height="22"><use href="#bell"/></svg>
      <span class="badge">3</span>
    </header>
    <h1 class="page-title">New Material Order</h1>
    <div class="card" style="top:157px;height:780px"></div>
    <div class="steps">
      <div class="step" style="width:168px"><svg width="12" height="10"><use href="#tick"/></svg>Date and Start</div>
      <div class="step active" style="width:168px"><svg width="12" height="10"><use href="#tick"/></svg>Destination</div>
      <div class="step todo" style="width:116px">Material</div>
      <div class="step" style="width:110px"><svg width="12" height="10"><use href="#tick"/></svg>Trucks</div>
      <div class="step" style="width:110px"><svg width="12" height="10"><use href="#tick"/></svg>Rates</div>
      <div class="step todo" style="width:135px">Summary</div>
      <svg class="step-edit" width="28" height="28"><use href="#pencil"/></svg>
    </div>
    <label class="field-label" style="left:138px;top:228px">PO/Job <span class="req">*</span></label>
    <div class="field" style="left:138px;top:260px;width:402px">12<span class="ctl" style="right:28px"><svg width="8" height="8"><use href="#clear"/></svg></span></div>
    <label class="field-label" style="left:582px;top:228px">Destination <span class="req">*</span></label>
    <div class="field" style="left:568px;top:260px;width:402px;padding-left:23px">RTB Plant 12 -Millbrook<span class="ctl" style="right:14px"><svg width="8" height="8"><use href="#clear"/></svg></span></div>
    <label class="field-label" style="left:138px;top:328px">Address <span class="req">*</span></label>
    <div class="field" style="left:138px;top:360px;width:833px">2109-Lorem ipsum dolor sit amet, consectetur adipiscing elit</div>
    <label class="field-label" style="left:138px;top:428px">Job Site Contact <span class="req">*</span></label>
    <div class="field" style="left:138px;top:460px;width:402px">02/27/2021<span class="ctl" style="right:18px"><svg width="8" height="8"><use href="#clear"/></svg><svg width="8" height="5"><use href="#caret"/></svg></span></div>
    <label class="field-label" style="left:568px;top:428px">Contact Number <span class="req">*</span></label>
    <div class="field" style="left:568px;top:460px;width:402px;padding-left:23px">(555) 555 0142<span class="ctl" style="right:14px"><svg width="8" height="8"><use href="#clear"/></svg><svg width="8" height="5"><use href="#caret"/></svg></span></div>
    <div class="btn outline" style="left:139px;top:530px;width:246px"><svg width="12" height="12"><use href="#plus"/></svg>ADD SECOND DESTINATION</div>
    <label class="field-label" style="left:138px;top:603px">Billing Job Site <span class="req">*</span></label>
    <div class="field" style="left:138px;top:635px;width:402px">2109-Ridgeway US 18/SR 5<span class="ctl" style="right:18px"><svg width="8" height="5"><use href="#caret"/></svg></span></div>
    <label class="field-label" style="left:567px;top:603px">Phase Code <span class="req">*</span></label>
    <div class="field" style="left:568px;top:635px;width:402px;padding-left:23px">01.0015..FIELD EN...<span class="ctl" style="right:14px"><svg width="8" height="8"><use href="#clear"/></svg><svg width="8" height="5"><use href="#caret"/></svg></span></div>
    <label class="field-label" style="left:138px;top:703px">Prevailing Wage?</label>
    <div class="toggle" style="left:138px;top:743px"><span class="off">YES</span><span class="on">NO</span></div>
    <div class="btn cancel" style="left:139px;top:852px">CANCEL</div>
    <div class="btn continue" style="left:833px;top:852px">CONTINUE</div>
    <footer class="footer" style="top:966px">© 2021 Companyname.All Rights Reserved &nbsp;|&nbsp; Privacy Policy &nbsp;|&nbsp; Terms and Use</footer>
  </section>
</div>
</body>
</html>
```